Creative Realtor Business Card Design

I need a creative business card.... I would like it to be larger than the normal size...heavy stock.... colorful...
As you are probably aware, there are tons of realtors, and most of their cards ALL look alike.. potential clients are looking for agents that are professional, but are different.
Cards are a form of advertising and I need your help to make mine stand out in a professional, classy way.
I don't need to use the harbor sage realty logo, my personal logo is MORE important for branding purposes. OR..what is your opinion?
YOU DESIGN FOR ME PLEASE! If I could do what you do I would.... I can't and I need your professional help.

                                        If you think I need the card to be double sided so it doesn't look busy by all means I will happily accept double sided. 

I am very interested in a more "creative" card than a standard run of the mill realtor card.    I care about my clients LONG after the sale has closed!

                                   

THANK YOU SO MUCH FOR YOUR EFFORTS AND TALENTS....I APPRECIATE IT SO MUCH! 

                                        Would it be possible to use my theme of my logo to design my card?

                                            Where Keys Meet Kindred Spirits

                              

 

Please make cards larger size .... See this link for ideas that appeal to me. Thank you for your interest.

https://www.lookwidely.example/find?q=examples+of+unique+business+cards&mode=img&ref=7QpL2xV9

I want my card to stand out in size and design...

Thank you so much for your hard work for me.

Lorna

 

Reason: I learned that many designers are very busy. I am providing more time and money in hopes that designers will find it an attractive enough challenge to participate. My business cards are one of my most important marketing materials...I NEED THEM TO BE DISTINCTIVE, CLASSY, and INFORMATIVE. Thank you SO MUCH....and I will be anxiously awaiting your great designs... Lorna

Hello Designers,

Thank you to all you creative people that have kindly offered to submit your creative design(s) for my business card.  I view your designs as your creative artwork. I am anxious to see where your creativity leads you.

I wanted to share with you that my logo was something I personally designed after being in business for 3  years. ( I did have to have a professionals like yourselves draw it for me). The design and logo captured perfectly how I felt about my work ...helping individuals, such as you, find a home.  A house is easy to find, but a home is a place that has "good" energy ... a place where you feel comfortable and can grow.  A place that just "Feels right!"  It's one of those things that you just KNOW when it is right! 

I hope by sharing this bit of information about me can help you creatively design my card for me...I care for my clients LONG after the transaction has closed and they are in their home. Thank you again for taking the time to work on my design. I have been adding money so that your time spent on my card is worth it.

I do need my card soon...so please, if you have a design...submit it!

Kind Regards,

Lorna

Target Market(s)

I have a variety of clients from a mobile home of $35,000 to an estate property for $5M. I feel comfortable working with all types of people...I love my job...I love helping people find the right home because we all know how our home environment affects our well being.

Industry/Entity Type

Advertising

Contact Information for Business Card

Lorna Pratley, Realtor
Harbor Sage Realty
"Where Keys Meet Kindred Spirits"
www.lornanestfinder.example
lpratley@mailbarn.example
(555) 418-2093
BRE #04872351, Exp. 8/15

Colors

Designer to choose colors to be used in the design.

Requirements
Must have
• By law, my license number information MUST be on my card.
Nice to have
• I would love card to be memorable...if that is possible for a business card. Also, I would like my card to be larger than the average card. Not sure that is possible either.

```html
<!DOCTYPE html>
<html lang="en">
<head>
<meta charset="utf-8">
<title>Harbor Sage Realty – Business Card</title>
<link rel="stylesheet" href="https://fonts.googleapis.com/css2?family=Arimo:wght@400;700&family=Ubuntu:wght@500;700&display=swap">
<style>
  :root{
    --sky:#bfe2f6;
    --ocean:#0277bd;
    --sage-ring:#d9e5b9;
    --white:#ffffff;
    --brand-blue:#1c7cc4;
    --ink:#2b2a14;
    --grey:#6d6d6d;
    --sun:#f5e93f;
    --faint-logo:#e4eef6;
    --blush:#f0a090;
    --teal:#4b7f7a;
  }
  *{margin:0;padding:0;box-sizing:border-box}
  html,body{width:1200px;height:801px;overflow:hidden;background:var(--white)}
  .canvas{position:relative;width:1200px;height:801px;background:var(--white)}
  .card{position:absolute;overflow:hidden}
  .card-front{background:var(--sky)}
  .card-front--rings{left:32px;top:66px;width:556px;height:324px}
  .card-front--plain{left:38px;top:419px;width:555px;height:324px}
  .card-front svg,.card-back svg{display:block;width:100%;height:100%}
  .card-back{left:628px;top:236px;width:542px;height:297px;background:var(--white)}
  .ring{fill:none;stroke:var(--sage-ring);stroke-width:30}
  .band{fill:var(--ocean)}
  .seal{fill:var(--white)}
  .seal-name{font-family:"Arimo",sans-serif;font-weight:700;font-size:21px;fill:var(--brand-blue);text-anchor:middle;letter-spacing:1.5px}
  .faint-seal{fill:var(--faint-logo)}
  .agent-name{font-family:"Ubuntu",sans-serif;font-weight:700;font-size:24px;fill:var(--brand-blue)}
  .agent-role{font-family:"Arimo",sans-serif;font-size:13.5px;fill:var(--grey)}
  .tagline{font-family:"Arimo",sans-serif;font-size:17px;fill:var(--ink)}
  .license{font-family:"Arimo",sans-serif;font-size:16px;fill:var(--ink)}
  .contact-line{font-family:"Arimo",sans-serif;font-size:13px;fill:var(--grey)}
  .phone{font-family:"Ubuntu",sans-serif;font-weight:500;font-size:23px;fill:var(--brand-blue);letter-spacing:1px}
  .expiry{font-family:"Arimo",sans-serif;font-size:17px;fill:var(--ink)}
  .sun-bar{fill:var(--sun)}
  .personal-dot{fill:var(--blush)}
  .personal-name{font-family:"Arimo",sans-serif;font-size:11px;fill:var(--teal);letter-spacing:.5px}
</style>
</head>
<body>
<main class="canvas">

  <section class="card card-front card-front--rings" aria-label="Card front with rings">
    <svg viewBox="32 66 556 324">
      <circle class="ring" cx="298" cy="222" r="250"/>
      <circle class="ring" cx="298" cy="222" r="168"/>
      <rect class="band" x="32" y="175" width="556" height="94"/>
      <circle class="seal" cx="298" cy="222" r="100"/>
      <text class="seal-name" x="298" y="212">HARBOR SAGE</text>
      <text class="seal-name" x="298" y="242">REALTY</text>
    </svg>
  </section>

  <section class="card card-front card-front--plain" aria-label="Card front">
    <svg viewBox="38 419 555 324">
      <rect class="band" x="38" y="529" width="555" height="94"/>
      <circle class="seal" cx="305" cy="576" r="100"/>
      <text class="seal-name" x="305" y="566">HARBOR SAGE</text>
      <text class="seal-name" x="305" y="596">REALTY</text>
    </svg>
  </section>

  <section class="card card-back" aria-label="Card back">
    <svg viewBox="628 236 542 297">
      <defs>
        <path id="arc-name" d="M755.1 278.8 A150 150 0 0 0 975 369.9"/>
        <path id="arc-role" d="M705.1 285 A200 200 0 0 0 1053.2 368.6"/>
        <path id="arc-tagline" d="M656.3 265.6 A245 245 0 0 0 1057.5 427.7"/>
        <path id="arc-license" d="M927.8 397.6 A160 160 0 0 0 1050.4 185.3"/>
        <path id="arc-contact" d="M889.1 447.7 A208 208 0 0 0 1104.8 203.9"/>
        <path id="arc-phone" d="M877.2 501 A262 262 0 0 0 1146.2 329.6"/>
        <path id="arc-expiry" d="M1082.8 436 A268 268 0 0 0 1168 240"/>
      </defs>

      <circle class="faint-seal" cx="900" cy="290" r="90"/>

      <text class="agent-name"><textPath href="#arc-name">Lorna Pratley</textPath></text>
      <text class="agent-role"><textPath href="#arc-role">Realtor Harbor Sage Realty</textPath></text>
      <text class="tagline"><textPath href="#arc-tagline">"Where Keys Meet Kindred Spirits"</textPath></text>
      <text class="license"><textPath href="#arc-license">BRE #04872351</textPath></text>
      <text class="contact-line"><textPath href="#arc-contact">lpratley@mailbarn.example • www.lornanestfinder.example</textPath></text>
      <text class="phone"><textPath href="#arc-phone">(555) 418-2093</textPath></text>
      <text class="expiry"><textPath href="#arc-expiry">Exp. 8/15</textPath></text>

      <circle class="personal-dot" cx="693" cy="470" r="14"/>
      <text class="personal-name" x="693" y="505" text-anchor="middle">LORNA PRATLEY</text>

      <rect class="sun-bar" x="628" y="516" width="542" height="17"/>
    </svg>
  </section>

</main>
</body>
</html>
```